It must be unique & Proffessional
VORNA GROUP
# 130 Very nice, could you please use the “symbols” for Phone, cellphone and so on, instead of writing “p:” and “c:”. You did that by # 69 :-)
Thanks for all your very creative suggestions.
A general comment:
- Please correct the “projektchef” to “Direktør”
- Please add at fixed telephone number +45 62 18 37 51
- Please add “+45” in front of the cellphone number
- Please make the envelope as window envelops, and logo bottom right corner
- On the A4 paper, we need the logo in top right corner
#61,Very good design, please make the backside as you’ve done by #64
#128Please leave the bottom of the paper free of text and colors, and add only one thin line 13 mm from the page bottom.
Again very good designs, thank you very much
Logo AI file is now uploaded :-)
Now we have our Logo ready, looking forward to see your suggestions for design :-)
TK/RWF Team
Logo is currently being designed, you can participate if you would like to :-)

```html
<!DOCTYPE html>
<html lang="en">
<head>
<meta charset="utf-8">
<title>VORNA GROUP – Business Card</title>
<link rel="stylesheet" href="https://fonts.googleapis.com/css2?family=Open+Sans:wght@400;600;700;800&display=swap">
<style>
  :root {
    --bg: #ece9e6;
    --card: #ffffff;
    --red: #c4161c;
    --red-dark: #8e0f13;
    --ink: #3a3a3a;
    --muted: #6b6b6b;
  }
  * { box-sizing: border-box; margin: 0; padding: 0; }
  html, body { width: 1200px; height: 758px; overflow: hidden; }
  body {
    background: var(--bg);
    font-family: "Open Sans", Arial, sans-serif;
    position: relative;
  }
  .card {
    position: absolute;
    width: 500px;
    height: 300px;
    background: var(--card);
    border-radius: 22px;
    overflow: hidden;
    box-shadow: 0 6px 18px rgba(0,0,0,0.15);
  }
  .card--front { left: 70px; top: 200px; }
  .card--back { left: 630px; top: 250px; }

  .front__band {
    height: 110px;
    background: linear-gradient(180deg, var(--red) 0%, var(--red-dark) 100%);
    position: relative;
  }
  .holder {
    position: absolute;
    left: 280px;
    top: 62px;
    color: #fff;
  }
  .holder__name { font-size: 15px; font-weight: 700; line-height: 1.2; }
  .holder__title { font-size: 11px; font-weight: 400; opacity: 0.9; }

  .brand {
    display: flex;
    align-items: center;
    gap: 10px;
  }
  .brand__mark {
    width: 22px;
    height: 22px;
    background: var(--red);
    flex: none;
  }
  .brand__name {
    font-weight: 800;
    color: var(--ink);
    letter-spacing: -0.5px;
    white-space: nowrap;
  }
  .card--front .brand {
    position: absolute;
    left: 26px;
    top: 168px;
  }
  .card--front .brand__mark { width: 18px; height: 18px; }
  .card--front .brand__name { font-size: 25px; }

  .contact {
    position: absolute;
    left: 280px;
    top: 122px;
    list-style: none;
    font-size: 11px;
    color: var(--muted);
    line-height: 1.45;
  }
  .contact li { display: flex; align-items: flex-start; gap: 8px; }
  .contact svg { width: 10px; height: 10px; margin-top: 3px; flex: none; fill: var(--muted); }
  .contact__group { margin-top: 10px; }

  .card--back .brand {
    position: absolute;
    left: 50%;
    top: 110px;
    transform: translateX(-50%);
  }
  .card--back .brand__mark { width: 28px; height: 28px; }
  .card--back .brand__name { font-size: 42px; }
  .back__web {
    position: absolute;
    left: 0; right: 0;
    top: 205px;
    text-align: center;
    font-size: 19px;
    font-weight: 600;
    letter-spacing: 1px;
    color: var(--ink);
  }
</style>
</head>
<body>

<section class="card card--front" aria-label="Business card front">
  <div class="front__band">
    <div class="holder">
      <p class="holder__name">Anders Holmgaard</p>
      <p class="holder__title">Direktør</p>
    </div>
  </div>

  <div class="brand">
    <span class="brand__mark"></span>
    <span class="brand__name">VORNA GROUP</span>
  </div>

  <ul class="contact">
    <li>
      <svg viewBox="0 0 10 10" aria-hidden="true"><path d="M2.2 0.6c0.5-0.3 1-0.2 1.3 0.3l1 1.6c0.3 0.5 0.1 1-0.3 1.3l-0.6 0.4c0.4 1 1.2 1.8 2.2 2.2l0.4-0.6c0.3-0.4 0.8-0.6 1.3-0.3l1.6 1c0.5 0.3 0.6 0.8 0.3 1.3l-0.6 0.9c-0.4 0.6-1.2 0.9-1.9 0.6C4.3 7.9 2.1 5.7 1.3 3.1 1 2.4 1.3 1.6 1.9 1.2z"/></svg>
      <span>+45 62 18 37 51</span>
    </li>
    <li>
      <svg viewBox="0 0 10 10" aria-hidden="true"><rect x="2.5" y="0" width="5" height="10" rx="1"/></svg>
      <span>+45 3186 5207</span>
    </li>
    <li>
      <svg viewBox="0 0 10 10" aria-hidden="true"><path d="M0 2h10v6H0z M0 2l5 3.5L10 2" fill="none" stroke="#6b6b6b" stroke-width="1"/></svg>
      <span>ah@vornagroup.com</span>
    </li>
    <li>
      <svg viewBox="0 0 10 10" aria-hidden="true"><circle cx="5" cy="5" r="4.3" fill="none" stroke="#6b6b6b" stroke-width="1"/><path d="M0.7 5h8.6M5 0.7v8.6" stroke="#6b6b6b" stroke-width="0.8"/></svg>
      <span>www.vornagroup.com</span>
    </li>
    <li class="contact__group">
      <svg viewBox="0 0 10 10" aria-hidden="true"><path d="M5 0.5L0 5h1.5v4.5h2.5V6.5h2v3h2.5V5H10z"/></svg>
      <span>Ravnsbjergvej 22<br>7100 Vejle, Denmark</span>
    </li>
  </ul>
</section>

<section class="card card--back" aria-label="Business card back">
  <div class="brand">
    <span class="brand__mark"></span>
    <span class="brand__name">VORNA GROUP</span>
  </div>
  <p class="back__web">www.vornagroup.com</p>
</section>

</body>
</html>
```